UI design for kiosk touch screen

We need a UI design for a touch screen device to be used by costumers in a store and show information about specific products. We're looking for a general concept to serve as a starting point and we're not expecting a fully coded design.
We envision a UI where it first shows a range of products; once touched, it should show information about the product which includes text, touchable photos, videos and document files. We're interested in the starting page and the product details page.
We are the suppliers of the device and not the owners of stores that will use them. The purpose of this design is for in-person demonstrations to potential clients or in ads so the design should be agnostic about the end product(s). You may freely pick random placeholder or fictional products and assets to showcase the design concept as long as they can be changed without compromising the design. You can use our logo (annexed) in the design as a placeholder but it's not necessary.
We're using web technologies to develop the UI so the same principles should apply, except some exceptions below:
- There's no need for a responsive design since the resolution is set at 1920x1080 on a 22'' monitor in landscape orientation.
- All interactions will be done using the touchscreen, so any interactive component needs to be large enough for navigation to be comfortable.
- The design should be visually engaging and eye-catching, more so than a regular website.
Physical shop owners.
Store
2 page

```html
<!DOCTYPE html>
<html lang="en">
<head>
<meta charset="utf-8">
<title>NOVATIK Kiosk UI</title>
<link href="https://fonts.googleapis.com/css2?family=Open+Sans:wght@400;600;700&display=swap" rel="stylesheet">
<style>
:root{
  --stage:#2b2b2b;
  --blue:#2a87f3;
  --white:#ffffff;
  --ink:#222831;
  --muted:#555;
  --orange:#f5821f;
  --line:#e3e3e3;
  --card-shadow:rgba(0,0,0,.12);
}
*{margin:0;padding:0;box-sizing:border-box}
html,body{width:1200px;height:1200px;overflow:hidden}
body{background:var(--stage);font-family:'Open Sans',sans-serif;position:relative;color:var(--white)}
.screen{position:absolute;background:var(--blue);overflow:hidden}
.screen--home{left:168px;top:40px;width:865px;height:513px}
.screen--detail{left:167px;top:573px;width:867px;height:587px}
.abs{position:absolute}
.topbar{position:absolute;left:0;top:0;right:0;height:48px;background:var(--white);color:var(--ink)}
.brand{position:absolute;left:20px;top:13px;display:flex;align-items:center;gap:6px}
.brand__mark{width:18px;height:18px;background:var(--blue);border-radius:3px}
.brand__name{font-weight:700;font-size:19px;color:var(--blue);letter-spacing:.5px}
.info-btn{position:absolute;left:494px;top:14px;width:122px;height:19px;border:1.5px solid var(--orange);color:var(--orange);font-size:9px;font-weight:600;display:flex;align-items:center;justify-content:center}
.divider{position:absolute;top:0;width:1px;height:48px;background:var(--line)}
.nav-item{position:absolute;top:16px;font-size:9px;font-weight:600;color:#444;display:flex;align-items:center;gap:9px}
.avatar{width:23px;height:23px;border:1.5px solid var(--orange);border-radius:50%;display:flex;align-items:center;justify-content:center}
.page-title{position:absolute;left:0;right:0;top:76px;text-align:center;font-weight:700;font-size:19px}
.page-sub{position:absolute;left:0;right:0;top:104px;text-align:center;font-size:14px}
.product{position:absolute;width:102px;height:137px;background:var(--white);color:var(--ink);text-align:center;box-shadow:0 2px 4px var(--card-shadow)}
.product__photo{height:84px;background:linear-gradient(160deg,#c9ced6,#6b7280)}
.product__name{font-size:8.5px;font-weight:700;margin-top:8px}
.product__text{font-size:7px;line-height:9px;color:var(--muted);margin-top:2px;padding:0 4px}
.copyright{position:absolute;font-size:7px;letter-spacing:.3px}
.kiosk-photo{left:57px;top:111px;width:88px;height:156px;background:linear-gradient(180deg,#f4f6f8,#cfd6de);border-radius:6px}
.share{left:58px;top:318px;width:80px;text-align:center;font-size:7.5px}
.share-icons{left:68px;top:348px;display:flex;gap:10px}
.share-icons span{width:16px;height:16px;border-radius:50%;background:var(--white)}
.detail-title{left:191px;top:88px;font-size:19px;font-weight:700}
.detail-sub{left:191px;top:115px;font-size:13px}
.price{left:191px;top:138px;font-size:16px;font-weight:700}
.detail-text{left:191px;top:162px;width:258px;font-size:7.5px;line-height:9px}
.vline{left:471px;top:124px;width:1px;height:146px;background:rgba(255,255,255,.25)}
.cta{left:192px;top:273px;width:79px;height:23px;border:1.5px solid var(--white);border-radius:12px;font-size:9.5px;font-weight:700;display:flex;align-items:center;justify-content:center}
.file{position:absolute;top:314px;width:77px;height:94px;background:var(--white);color:var(--ink);text-align:center;font-size:7.5px}
.file svg{display:block;margin:12px auto 8px}
.video{left:498px;top:90px;width:327px;height:202px;border-radius:4px;background:linear-gradient(120deg,#3a3f47,#5b6470 60%,#3b434d)}
.play{left:646px;top:177px}
.thumb{position:absolute;top:315px;width:86px;height:52px;border-radius:3px;background:linear-gradient(120deg,#3a3f47,#5e6772)}
.desc-title{left:191px;top:430px;font-size:17px;font-weight:700}
.desc-text{left:192px;top:462px;width:530px;font-size:7.5px;line-height:9px}
</style>
</head>
<body>

<section class="screen screen--home">
  <header class="topbar">
    <div class="brand"><span class="brand__mark"></span><span class="brand__name">NOVATIK</span></div>
    <div class="info-btn">Get More Information</div>
    <div class="divider" style="left:631px"></div>
    <div class="nav-item" style="left:650px">Send Message
      <svg width="17" height="14" viewBox="0 0 17 14"><path d="M1 1h15v9H7l-3 3v-3H1z" fill="none" stroke="#f5821f" stroke-width="1.2"/><circle cx="6" cy="5.5" r=".9" fill="#f5821f"/><circle cx="8.5" cy="5.5" r=".9" fill="#f5821f"/><circle cx="11" cy="5.5" r=".9" fill="#f5821f"/></svg>
    </div>
    <div class="divider" style="left:751px"></div>
    <div class="nav-item" style="left:762px;top:12px">Paul Harlow
      <span class="avatar"><svg width="11" height="11" viewBox="0 0 11 11"><circle cx="5.5" cy="3.5" r="2.3" fill="none" stroke="#333"/><path d="M1 10.5c0-2.5 2-4 4.5-4s4.5 1.5 4.5 4z" fill="none" stroke="#333"/></svg></span>
    </div>
  </header>

  <h1 class="page-title">NOVATIK PRODUCTS RANGE</h1>
  <p class="page-sub">Neque porro quisquam est qui dolorem ipsum</p>

  <article class="product" style="left:28px;top:148px"><div class="product__photo" role="img" aria-label="Tablet kiosk on a stand"></div><h3 class="product__name">Finibus Bonorum</h3><p class="product__text">vero eos et accusamus iusto odio dignissimos ducimus</p></article>
  <article class="product" style="left:146px;top:148px"><div class="product__photo" role="img" aria-label="Touch table kiosk with colourful screen"></div><h3 class="product__name">Finibus Bonorum</h3><p class="product__text">vero eos et accusamus iusto odio dignissimos ducimus</p></article>
  <article class="product" style="left:264px;top:148px"><div class="product__photo" role="img" aria-label="Row of kiosks in an exhibition hall"></div><h3 class="product__name">Finibus Bonorum</h3><p class="product__text">vero eos et accusamus iusto odio dignissimos ducimus</p></article>
  <article class="product" style="left:382px;top:148px"><div class="product__photo" role="img" aria-label="Wooden kiosk with tilted screen"></div><h3 class="product__name">Finibus Bonorum</h3><p class="product__text">vero eos et accusamus iusto odio dignissimos ducimus</p></article>
  <article class="product" style="left:500px;top:148px"><div class="product__photo" role="img" aria-label="Customer using a touch terminal"></div><h3 class="product__name">Finibus Bonorum</h3><p class="product__text">vero eos et accusamus iusto odio dignissimos ducimus</p></article>
  <article class="product" style="left:618px;top:148px"><div class="product__photo" role="img" aria-label="Shopper checking a phone"></div><h3 class="product__name">Finibus Bonorum</h3><p class="product__text">vero eos et accusamus iusto odio dignissimos ducimus</p></article>
  <article class="product" style="left:736px;top:148px"><div class="product__photo" role="img" aria-label="Shopper holding a tablet in a store"></div><h3 class="product__name">Finibus Bonorum</h3><p class="product__text">vero eos et accusamus iusto odio dignissimos ducimus</p></article>

  <article class="product" style="left:28px;top:299px"><div class="product__photo" role="img" aria-label="Counter tablets on swivel stands"></div><h3 class="product__name">Finibus Bonorum</h3><p class="product__text">vero eos et accusamus iusto odio dignissimos ducimus</p></article>
  <article class="product" style="left:146px;top:299px"><div class="product__photo" role="img" aria-label="Tablet display on a shop counter"></div><h3 class="product__name">Finibus Bonorum</h3><p class="product__text">vero eos et accusamus iusto odio dignissimos ducimus</p></article>
  <article class="product" style="left:264px;top:299px"><div class="product__photo" role="img" aria-label="Person tapping a wall screen"></div><h3 class="product__name">Finibus Bonorum</h3><p class="product__text">vero eos et accusamus iusto odio dignissimos ducimus</p></article>
  <article class="product" style="left:382px;top:299px"><div class="product__photo" role="img" aria-label="Shopper touching a kiosk screen"></div><h3 class="product__name">Finibus Bonorum</h3><p class="product__text">vero eos et accusamus iusto odio dignissimos ducimus</p></article>
  <article class="product" style="left:500px;top:299px"><div class="product__photo" role="img" aria-label="Commuter using a phone on a train"></div><h3 class="product__name">Finibus Bonorum</h3><p class="product__text">vero eos et accusamus iusto odio dignissimos ducimus</p></article>
  <article class="product" style="left:618px;top:299px"><div class="product__photo" role="img" aria-label="Shopper using a vending screen"></div><h3 class="product__name">Finibus Bonorum</h3><p class="product__text">vero eos et accusamus iusto odio dignissimos ducimus</p></article>
  <article class="product" style="left:736px;top:299px"><div class="product__photo" role="img" aria-label="Hand pressing a terminal keypad"></div><h3 class="product__name">Finibus Bonorum</h3><p class="product__text">vero eos et accusamus iusto odio dignissimos ducimus</p></article>

  <p class="copyright" style="left:0;right:0;top:480px;text-align:center">Copyright@2017 NOVATIK. All rights reserved.</p>
</section>

<section class="screen screen--detail">
  <header class="topbar">
    <div class="brand"><span class="brand__mark"></span><span class="brand__name">NOVATIK</span></div>
    <div class="info-btn">Get More Information</div>
    <div class="divider" style="left:631px"></div>
    <div class="nav-item" style="left:650px">Send Message
      <svg width="17" height="14" viewBox="0 0 17 14"><path d="M1 1h15v9H7l-3 3v-3H1z" fill="none" stroke="#f5821f" stroke-width="1.2"/><circle cx="6" cy="5.5" r=".9" fill="#f5821f"/><circle cx="8.5" cy="5.5" r=".9" fill="#f5821f"/><circle cx="11" cy="5.5" r=".9" fill="#f5821f"/></svg>
    </div>
    <div class="divider" style="left:751px"></div>
    <div class="nav-item" style="left:762px;top:12px">Paul Harlow
      <span class="avatar"><svg width="11" height="11" viewBox="0 0 11 11"><circle cx="5.5" cy="3.5" r="2.3" fill="none" stroke="#333"/><path d="M1 10.5c0-2.5 2-4 4.5-4s4.5 1.5 4.5 4z" fill="none" stroke="#333"/></svg></span>
    </div>
  </header>

  <div class="abs kiosk-photo" role="img" aria-label="White freestanding kiosk product"></div>
  <p class="abs share">Share On</p>
  <div class="abs share-icons"><span></span><span></span><span></span></div>

  <h1 class="abs detail-title">FINIBUS BONORUM</h1>
  <p class="abs detail-sub">Neque porro quisquam est qui dolorem ipsum</p>
  <p class="abs price">$546</p>
  <p class="abs detail-text">On the other hand, we denounce with righteous indignation and dislike men who are so beguiled and demoralized by the charms of pleasure of the moment, so blinded by desire, that they cannot foresee the pain and trouble that are bound to ensue; and equal blame belongs to those who fail in their duty through weakness of will, which is the same as saying through shrinking from toil and pain. These cases are perfectly simple and easy to distinguish. vero eos et accusamus et iusto odio dignissimos ducimus qui blanditiis praesentium voluptatum deleniti atque corrupti quos dolores et quas molestias excepturi sint occaecati cupiditate non provident.</p>
  <div class="abs vline"></div>
  <div class="abs cta">Get Started</div>

  <div class="file" style="left:192px">
    <svg width="40" height="56" viewBox="0 0 40 56"><path d="M1 1h28l10 10v44H1z" fill="#fff" stroke="#2a87f3" stroke-width="1.5"/><path d="M29 1v10h10" fill="none" stroke="#2a87f3" stroke-width="1.5"/><g stroke="#2a87f3" stroke-width="2"><path d="M6 14h28M6 19h28M6 24h28M6 29h28M6 34h28M6 39h28M6 44h28M6 49h28"/></g></svg>File Name</div>
  <div class="file" style="left:278px">
    <svg width="40" height="56" viewBox="0 0 40 56"><path d="M1 1h28l10 10v44H1z" fill="#fff" stroke="#2a87f3" stroke-width="1.5"/><path d="M29 1v10h10" fill="none" stroke="#2a87f3" stroke-width="1.5"/><g stroke="#2a87f3" stroke-width="2"><path d="M6 14h28M6 19h28M6 24h28M6 29h28M6 34h28M6 39h28M6 44h28M6 49h28"/></g></svg>File Name</div>
  <div class="file" style="left:364px">
    <svg width="40" height="56" viewBox="0 0 40 56"><path d="M1 1h28l10 10v44H1z" fill="#fff" stroke="#2a87f3" stroke-width="1.5"/><path d="M29 1v10h10" fill="none" stroke="#2a87f3" stroke-width="1.5"/><g stroke="#2a87f3" stroke-width="2"><path d="M6 14h28M6 19h28M6 24h28M6 29h28M6 34h28M6 39h28M6 44h28M6 49h28"/></g></svg>File Name</div>

  <div class="abs video" role="img" aria-label="Video of a shopper using a wall touch screen"></div>
  <svg class="abs play" width="30" height="22" viewBox="0 0 30 22"><rect x="1" y="1" width="28" height="20" rx="5" fill="none" stroke="#fff" stroke-width="2"/><path d="M12 6l8 5-8 5z" fill="#fff"/></svg>
  <div class="thumb" style="left:496px" role="img" aria-label="Video thumbnail"></div>
  <div class="thumb" style="left:592px" role="img" aria-label="Video thumbnail"></div>
  <div class="thumb" style="left:687px" role="img" aria-label="Video thumbnail"></div>

  <h2 class="abs desc-title">PRODUCT DISCRIPTION FINIBUS BONORUM</h2>
  <p class="abs desc-text">On the other hand, we denounce with righteous indignation and dislike men who are so beguiled and demoralized by the charms of pleasure of the moment, so blinded by desire, that they cannot foresee the pain and trouble that are bound to ensue; and equal blame belongs to those who fail in their duty through weakness of will, which is the same as saying through shrinking from toil and pain. These cases are perfectly simple and easy to distinguish. vero eos et accusamus et iusto odio dignissimos ducimus qui blanditiis praesentium voluptatum deleniti atque corrupti quos dolores et quas molestias excepturi sint occaecati cupiditate non provident.</p>
  <p class="copyright" style="left:192px;top:541px">Copyright@2017 NOVATIK. All rights reserved.</p>
</section>

</body>
</html>
```